The Quiet Compass
Zielgruppe
Das Bundesforum Seelenheilkundiger Praxen e. V. (BFSP) ist ein Interessenverband mit 1.400 Mitgliedern, der sich für die Belange von psychotherapeutisch tätigen Psychologen, Ärzten und Kinder- und Jugendlichen-Psychotherapeuten einsetzt. Das Bundesforum Seelenheilkundiger Praxen wurde als Berufsverband am 2. Mai 2019 in Bonn gegründet.
Aufgabenstellung
Titel: The Quiet Compass - Das Arbeitsbuch der selten genutzten und vergessenen therapeutischen Werkzeuge im Behandlungsalltag
Kategorie: Sachbuch
Zielgruppe: nur Psychotherapeuten
Covergestaltung: Cover soll neugierig machen, aber nicht marktschreierisch sein, AIDA-Regel berücksichtigen,
„Augenfänger“, dezente Farben, nicht zu grell
Buchformat: 22x15.5 cm, ca. 530 Normseiten
Buchrücken: Titel und Autor
Ausführung: Hardcover, Softcover, Ebook
Autor: Rainer Holtkamp, Dipl.-Psychologe, ist Psychoanalytiker der Westfälischen Tiefenseelischen Gesellschaft, Kinder- und Jugendlichenpsychotherapeut, Psychologischer Psychotherapeut, Gruppenanalytiker, Lehrtherapeut und Supervisor. Neben seiner psychoanalytischen Ausbildung hat er noch Aus- und Weiterbildungen in Gruppentherapie, Gruppendynamik, Familientherapie, katathym imaginativer Psychotherapie und intensiver psychodynamischer Kurztherapie nach Davanloo. Seit 29 Jahren arbeitet er in seiner eigenen Praxis in Bonn. Neben seiner Praxistätigkeit arbeitet er als Gutachter im Antragsverfahren der gesetzlichen Krankenkassen und der Beihilfestellen. Er ist Gründer und 1. Vorsitzender des Bundesforums Seelenheilkundiger Praxen (BFSP) in Bonn.
Klappentext: „Wer liebt, was er tut, wird nie wieder arbeiten müssen.“ Ein kluger Aphorismus, der Konfuzius zugeschrieben wird. Psychotherapeuten lieben ihren Beruf. Dennoch ist die Arbeit mit kranken Menschen immer schwer und unberechenbar. Viele Erfahrungen und Erkenntnisse musste sich Rainer Holtkamp im Laufe seiner Berufstätigkeit von fast 30 Jahren selbst erarbeiten. In seiner Tätigkeit als Dozent und Supervisor konnte er viele Fragen der Kandidaten sammeln und daraus Interventionen erarbeiten. Interventionen, die meist in keinem Lehrbuch stehen. Mit vielen dieser Interventionen wird die psychotherapeutische Arbeit leichter und macht auch mehr Freude. Und wer mit Freude als Psychotherapeut in die Praxis geht, 'arbeitet' im Sinne ..

```html
<!DOCTYPE html>
<html lang="de">
<head>
<meta charset="utf-8">
<title>The Quiet Compass – Rainer Holtkamp</title>
<link rel="stylesheet" href="https://fonts.googleapis.com/css2?family=Jost:wght@300;400&display=swap">
<style>
  :root {
    --cover-red: #e8423d;
    --ink: #1d1d1b;
    --paper: #ffffff;
    --art-red: #e63a40;
    --art-white: #fbf4f4;
    --art-crimson: #c41f2e;
    --art-shadow: #7c1420;
  }
  html, body {
    margin: 0;
    padding: 0;
    width: 845px;
    height: 1200px;
    overflow: hidden;
    background: var(--cover-red);
  }
  .cover {
    position: relative;
    width: 845px;
    height: 1200px;
    background: var(--cover-red);
    overflow: hidden;
    font-family: "Jost", "Futura", sans-serif;
  }
  .author {
    position: absolute;
    top: 62px;
    left: 0;
    width: 100%;
    margin: 0;
    text-align: center;
    font-weight: 300;
    font-size: 33px;
    letter-spacing: 0.3px;
    color: var(--paper);
  }
  .title {
    position: absolute;
    top: 194px;
    left: 0;
    width: 100%;
    margin: 0;
    text-align: center;
    font-weight: 400;
    font-size: 104px;
    line-height: 92px;
    letter-spacing: 1px;
    color: var(--ink);
    text-transform: uppercase;
  }
  .subtitle {
    position: absolute;
    top: 410px;
    left: 0;
    width: 100%;
    margin: 0;
    text-align: center;
    font-weight: 300;
    font-size: 40px;
    line-height: 38.5px;
    color: var(--ink);
  }
  .artwork {
    position: absolute;
    left: 228px;
    top: 755px;
    width: 376px;
    height: 445px;
    display: block;
  }
</style>
</head>
<body>
  <main class="cover">
    <p class="author">Rainer Holtkamp</p>
    <h1 class="title">The Quiet<br>Compass</h1>
    <p class="subtitle">Das Arbeitsbuch<br>der selten genutzten<br>und vergessenen<br>therapeutischen Werkzeuge<br>im Behandlungsalltag</p>
    <svg class="artwork" viewBox="0 0 376 445" role="img" aria-label="Illustration: eine große weiße Hand reicht von unten nach oben, eine kleine rote Kinderhand liegt darauf, mit langem dunkelrotem Schatten nach rechts unten">
      <defs>
        <linearGradient id="artTones" x1="0" y1="0.1" x2="1" y2="0.9">
          <stop offset="0" stop-color="var(--art-red)"/>
          <stop offset="0.22" stop-color="var(--art-red)"/>
          <stop offset="0.42" stop-color="var(--art-white)"/>
          <stop offset="0.55" stop-color="var(--art-white)"/>
          <stop offset="0.72" stop-color="var(--art-crimson)"/>
          <stop offset="1" stop-color="var(--art-shadow)"/>
        </linearGradient>
      </defs>
      <rect width="376" height="445" fill="url(#artTones)"/>
    </svg>
  </main>
</body>
</html>
```